Flyer für Unterstützung in der Personalarbeit
Zielgruppe
HR Freelancer, bitte Dienstleistung für Unternehmen an, die temporär Unterstützung in der Personalarbeit (Personalprozesse, Recruiting, Lohn- und Gehaltsabrechnung, HR Management, Administration) benötigen.
Aufgabenstellung
Ich benötige einen mehrseitigen Flyer, der mich und meine Arbeit kurz vorstellt. Außerdem soll es in einem Teil darum gehen, warum ein HR Freelancer eine gute Wahl ist. Der Flyer/die Broschüre soll an Unternehmen versendet werden.
Ich wünsche mir ein modernes minimalistisches und dennoch ansprechendes Design. Ich benötige die Datei am Ende auch im Word Format, da ich zukünftig Referenzen und weitere Auftraggeber ergänzen muss.
Ich füge zudem verschiedene Bilder bei, dabei müssen nicht alle berücksichtigt werden.

```html
<!DOCTYPE html>
<html lang="de">
<head>
<meta charset="utf-8">
<title>HR-Freelancerin Flyer</title>
<link href="https://fonts.googleapis.com/css2?family=Open+Sans:ital,wght@1,300;1,800&family=Source+Sans+3:ital,wght@0,300;0,400;0,600;0,700;1,400;1,600&display=swap" rel="stylesheet">
<style>
:root{
  --teal:#0f6b72;
  --teal-soft:#6fa3a8;
  --beige:#e7ddd5;
  --light:#f3f1ef;
  --gray:#e3e1df;
  --dark:#2a1410;
  --ink:#2b2624;
  --white:#ffffff;
}
*{margin:0;padding:0;box-sizing:border-box}
html,body{width:1158px;height:1200px;overflow:hidden;background:#fff}
body{position:relative;font-family:"Source Sans 3",sans-serif;color:var(--ink)}
.abs{position:absolute}
.sheet{position:absolute;left:16px;width:1129px;box-shadow:0 4px 12px rgba(0,0,0,.18)}
.sheet--outside{top:42px;height:534px;background:var(--light)}
.sheet--inside{top:621px;height:534px;background:#fff}
.fold{position:absolute;width:1px;background:#333}
.photo{position:absolute}
.block{position:absolute}
.chevron{position:absolute}
.headline{font-family:"Open Sans",sans-serif;font-style:italic;color:#fff;line-height:17px}
.headline .light{font-weight:300;font-size:18px;display:block}
.headline .bold{font-weight:800;font-size:18px;display:block}
.invite{font-style:italic;font-size:8px;line-height:12.7px;color:var(--ink)}
.section-title{font-weight:300;color:var(--teal);letter-spacing:.3px}
.about{font-size:8.6px;line-height:12.6px;color:var(--teal);font-weight:400}
.contact{display:flex;align-items:center;gap:12px;font-size:8.8px;font-weight:600;color:var(--teal)}
.contact a{color:var(--teal);font-weight:400}
.contact svg{flex:none}
.brand{background:#000;color:#fff;display:flex;flex-direction:column;align-items:center;justify-content:center;gap:5px}
.brand__name{font-weight:300;font-size:15px;letter-spacing:.5px}
.brand__role{font-weight:300;font-size:7px;letter-spacing:.5px}
.band{color:#fff;font-size:7px;line-height:8px}
.band h4{font-size:8px;font-weight:700;letter-spacing:1px;margin-bottom:7px}
.band p{margin-bottom:6px;font-weight:600}
.band__claim{font-size:8.6px;line-height:12.4px;font-weight:600}
.vtitle{position:absolute;transform:rotate(-90deg);transform-origin:left top;color:#fff;font-weight:600;font-size:15px;line-height:21px;letter-spacing:1px;white-space:nowrap}
.col{position:absolute;font-size:7.3px;line-height:9.7px;color:var(--ink)}
.col p{margin-bottom:5.3px}
.col .lead{color:var(--teal);font-weight:700}
.services{font-size:7.3px;line-height:9.4px}
.services p{margin-bottom:5.3px}
.services b{font-weight:700;display:block}
.why-title{position:absolute;transform:rotate(-90deg);transform-origin:left top;color:var(--teal);font-weight:400;font-size:10.5px;letter-spacing:.8px;white-space:nowrap}
.feature-box{background:rgba(120,104,98,.72);color:#fff;padding:22px 10px 0 10px}
.feature-box h3{font-weight:300;font-style:italic;font-size:20px;margin-bottom:4px;letter-spacing:.3px}
.feature-box .k{font-style:italic;font-weight:600;font-size:11.4px;line-height:13px}
.feature-box .v{font-weight:600;font-size:11.4px;line-height:12.5px;margin-bottom:4px}
</style>
</head>
<body>

<div class="fold" style="left:392px;top:0;height:42px"></div>
<div class="fold" style="left:769px;top:0;height:42px"></div>
<div class="fold" style="left:393px;top:578px;height:45px"></div>
<div class="fold" style="left:769px;top:578px;height:52px"></div>
<div class="fold" style="left:393px;top:1157px;height:43px"></div>
<div class="fold" style="left:770px;top:1157px;height:43px"></div>

<!-- OUTSIDE -->
<section class="sheet sheet--outside">
  <div class="photo" role="img" aria-label="Holzwürfel mit HR-Symbolen, von einer Hand gestapelt" style="left:0;top:0;width:138px;height:183px;background:linear-gradient(160deg,#a9c6c5,#c9d5d0 60%,#d9cbb6)"></div>
  <div class="block" style="left:138px;top:0;width:238px;height:183px;background:var(--beige)"></div>
  <div class="block" style="left:138px;top:183px;width:377px;height:88px;background:var(--teal-soft)"></div>
  <div class="headline abs" style="left:164px;top:195px">
    <span class="light">Lassen Sie uns</span>
    <span class="light">Ihre HR-Themen</span>
    <span class="bold">gemeinsam</span>
    <span class="bold">erfolgreich gestalten!</span>
  </div>
  <div class="block" style="left:138px;top:271px;width:238px;height:263px;background:var(--gray)"></div>
  <svg class="chevron" style="left:97px;top:309px" width="36" height="36" viewBox="0 0 36 36"><path d="M0 0h8l12 18-12 18H0l12-18z M16 0h8l12 18-12 18h-8l12-18z" fill="var(--teal)"/></svg>
  <p class="invite abs" style="left:153px;top:304px;width:136px">Kontaktieren Sie mich gerne für ein unverbindliches Gespräch – ich freue mich darauf, Ihre HR-Prozesse zu optimieren und Ihr Team erfolgreich zu unterstützen.</p>

  <svg class="chevron" style="left:457px;top:42px" width="36" height="36" viewBox="0 0 36 36"><path d="M0 0h8l12 18-12 18H0l12-18z M16 0h8l12 18-12 18h-8l12-18z" fill="var(--teal)"/></svg>
  <div class="block" style="left:515px;top:0;width:238px;height:271px;background:var(--beige)"></div>
  <h2 class="section-title abs" style="left:527px;top:144px;font-size:26px">ÜBER MICH</h2>
  <p class="about abs" style="left:526px;top:180px;width:218px">Ich bin eine HR-Generalistin mit über 10 Jahren Erfahrung. Als HR-Freelancerin helfe ich Unternehmen dabei, ihre HR-Prozesse zu optimieren und maßgeschneiderte Lösungen zu finden. Ob Personalbetreuung, Recruiting oder Prozess­verbesserungen – ich kenne die Herausforderungen und packe sie mit Leidenschaft an.</p>
  <div class="photo" role="img" aria-label="Foto der Freelancerin auf einer Treppe mit Smartphone" style="left:376px;top:271px;width:139px;height:222px;background:linear-gradient(135deg,#d9d4cc,#b9ad9f 55%,#6a5a4e)"></div>
  <div class="block" style="left:515px;top:271px;width:238px;height:222px;background:var(--gray)"></div>
  <div class="abs" style="left:576px;top:302px;display:flex;flex-direction:column;gap:17px">
    <div class="contact"><svg width="11" height="11" viewBox="0 0 12 12"><circle cx="6" cy="6" r="5.4" fill="none" stroke="var(--teal)" stroke-width=".8"/><path d="M4 3.3l1 1.4-.6.6c.4.9 1 1.5 1.9 1.9l.6-.6 1.4 1-.6 1c-2.2-.2-4.5-2.5-4.7-4.7z" fill="var(--teal)"/></svg>0170 / 55 81 04 27 (Messenger)</div>
    <div class="contact"><svg width="11" height="11" viewBox="0 0 12 12"><circle cx="6" cy="6" r="5.4" fill="none" stroke="var(--teal)" stroke-width=".8"/><text x="6" y="8.3" font-size="6.5" text-anchor="middle" fill="var(--teal)" font-family="sans-serif">@</text></svg>mail@lenavossberg.de</div>
    <div class="contact"><svg width="11" height="11" viewBox="0 0 12 12"><circle cx="6" cy="6" r="5.4" fill="none" stroke="var(--teal)" stroke-width=".8"/><circle cx="6" cy="6" r="2" fill="var(--teal)"/></svg><a href="#">Lena Vossberg</a></div>
    <div class="contact"><svg width="11" height="11" viewBox="0 0 12 12"><circle cx="6" cy="6" r="5.4" fill="none" stroke="var(--teal)" stroke-width=".8"/><path d="M6 2.8a2 2 0 0 1 2 2c0 1.5-2 3.8-2 3.8S4 6.3 4 4.8a2 2 0 0 1 2-2z" fill="var(--teal)"/></svg>Kranichsfelde, Berlin</div>
    <div class="contact"><svg width="11" height="11" viewBox="0 0 12 12"><circle cx="6" cy="6" r="5.4" fill="none" stroke="var(--teal)" stroke-width=".8"/><circle cx="6" cy="6" r="3" fill="none" stroke="var(--teal)" stroke-width=".6"/><path d="M3 6h6M6 3v6" stroke="var(--teal)" stroke-width=".6"/></svg><a href="#">lenavossberg.de</a></div>
  </div>
  <div class="block" style="left:376px;top:493px;width:377px;height:41px;background:var(--dark)"></div>

  <div class="photo" role="img" aria-label="Porträt der Freelancerin im dunklen Blazer vor heller Wand" style="left:753px;top:0;width:376px;height:422px;background:linear-gradient(100deg,#d8cfc6 0%,#cfc4b9 40%,#8a7466 62%,#3b302c 78%,#d9d3cc 100%)"></div>
  <div class="brand abs" style="left:785px;top:105px;width:96px;height:96px">
    <span class="brand__name">lena vossberg</span>
    <span class="brand__role">HR Freelancer</span>
  </div>
  <div class="block band" style="left:753px;top:422px;width:376px;height:112px;background:var(--teal)">
    <div class="abs" style="left:32px;top:10px;width:86px">
      <h4 style="font-style:italic">EXPERTISEN</h4>
      <p>HR Generalist / Personalbetreuung</p>
      <p>Full Life Cycle Recruiting</p>
      <p>Fließende Englisch-<br>kenntnisse</p>
    </div>
    <div class="abs" style="left:130px;top:8px;width:1px;height:96px;background:rgba(255,255,255,.6)"></div>
    <div class="abs" style="left:138px;top:10px;width:98px">
      <p>Zusammenarbeit mit Arbeit­nehmervertretungen</p>
      <p>Einführung und Betreuung von Bewerbermanagement­systemen Vorbereitende Lohn- und Gehaltsabrech­nung (PayDesk)</p>
      <p>Berufserfahrung in verschie­denen Dienstleistungs­branchen</p>
    </div>
    <div class="abs" style="left:245px;top:8px;width:1px;height:96px;background:rgba(255,255,255,.6)"></div>
    <div class="abs" style="left:254px;top:10px;width:100px">
      <h4 style="letter-spacing:.3px">LENA VOSSBERG</h4>
      <p class="band__claim">Ihre HR-Freelancerin für maßgeschneiderte Lösungen</p>
    </div>
  </div>
</section>

<!-- INSIDE -->
<section class="sheet sheet--inside">
  <svg class="abs" style="left:116px;top:0" width="309" height="534" viewBox="0 0 309 534">
    <rect x="0" y="271" width="309" height="263" fill="var(--gray)"/>
    <polygon points="0,0 40,0 145,70 260,0 309,0 309,12 145,120 0,40" fill="#e9eef0"/>
    <polygon points="120,100 145,120 260,40 309,75 309,200 210,140 145,185 0,90 0,40 40,60" fill="#e9eef0" opacity=".9"/>
    <polygon points="170,190 260,140 309,170 309,260 260,230 170,280" fill="#e9eef0" opacity=".8"/>
  </svg>
  <div class="block" style="left:0;top:0;width:116px;height:534px;background:var(--teal-soft)"></div>
  <svg class="chevron" style="left:0;top:67px" width="58" height="81" viewBox="0 0 58 81"><path d="M0 14l18 26L0 66z M18 0h14l26 40-26 41H18l26-41z" fill="var(--teal)"/></svg>
  <div class="vtitle" style="left:56px;top:268px">Berufliche Stationen und<br>relevante Projekterfahrung</div>
  <div class="col" style="left:139px;top:72px;width:100px">
    <p class="lead">HR-Freelancerin (seit 2024):</p>
    <p>Interim HR Operations:</p>
    <p>Betreuung eines Unterneh­mens mit ca. 10.000 Mit­arbeitenden</p>
    <p>Bearbeitung von HR Opera­tions Anfragen</p>
    <p>Beratung in übergreifenden HR Prozessen zu Disziplinar­maßnahmen, Bescheini­gungswesen und Verträgen</p>
    <p>Administrative und orga­nisatorische Beratung der Teamleitung</p>
    <p>Beratung hinsichtlich der vor- und nachbereitenden Payroll</p>
    <p class="lead">Senior HR Freelancer:</p>
    <p>Unterstützung eines Online-Marketing-Unternehmens mit ca. 200 Mitarbeitenden</p>
    <p>Beratung hinsichtlich opera­tiver Personalthemen</p>
    <p>Optimierung des Onboar­dings und der Personalbe­treuung</p>
    <p>HR-Generalistin bei Nordlicht Service Solutions (2018 – 2023):</p>
    <p>Personalbetreuung und -verwaltung von ca. 650 Mitarbeitenden</p>
    <p>Vorbereitung von Lohn- und Gehaltsabrechnungen (PayDesk)</p>
  </div>
  <div class="col" style="left:247px;top:72px;width:100px">
    <p>Koordination von Personal­vorgängen (Einstellungen, Vertragsänderungen, Aus­tritte)</p>
    <p>Ansprechpartnerin für Mit­arbeitende und Führungs­kräfte</p>
    <p>Durchführung des BEM-Pro­zesses zur Wiedereingliede­rung nach Krankheitszeiten</p>
    <p>Recruitment Manager bei Modehaus Veltra (2014 – 2018):</p>
    <p>Leitung des deutschland­weiten Recruitment-Teams</p>
    <p>Gesamtverantwortung für den Bewerbungsprozess: Stellenanzeigen, Auswahl­gespräche</p>
    <p>Durchführung von High Volume Recruitings bei Neu­eröffnungen (ca. 300 Mit­arbeitende)</p>
    <p>Unterstützung von Füh­rungskräften bei der Rekru­tierung und Teamaufbau</p>
    <p>HR Coordinator bei der Halden Hotelgruppe (2013 – 2014):</p>
    <p>Personaladministration und Bewerbermanagement</p>
    <p>Vorbereitende Lohnabrech­nung und Unterstützung des externen Lohnbüros</p>
    <p>Pflege von Personalakten und Stammdaten</p>
    <p>Weiterentwicklung und Implementierung von HR-Prozessen</p>
  </div>

  <div class="block" style="left:377px;top:0;width:238px;height:270px;background:var(--beige)"></div>
  <svg class="chevron" style="left:432px;top:23px" width="36" height="36" viewBox="0 0 36 36"><path d="M0 0h8l12 18-12 18H0l12-18z M16 0h8l12 18-12 18h-8l12-18z" fill="var(--teal)"/></svg>
  <h2 class="section-title abs" style="left:435px;top:68px;font-size:12px;font-weight:400">LEISTUNGEN IM ÜBERBLICK</h2>
  <div class="col services" style="left:435px;top:90px;width:150px">
    <p><b>Interim HR &amp; Projektmanagement:</b>Temporäre Übernahme von HR-Aufgaben zur Überbrückung von Vakanzen, Unter­stützung in Projekten oder bei Engpässen.</p>
    <p><b>Onboarding-Prozesse:</b>Gestaltung und Optimierung von Onboar­ding-Prozessen zur schnellen und effekti­ven Integration neuer Mitarbeiter.</p>
    <p><b>Recruiting &amp; High Volume Recruiting:</b>Rekrutierung der passenden Talente für Ihr Unternehmen, inklusive vollständigem Bewerbermanagement und Vorstellungs­gesprächen.</p>
    <p><b>Vorbereitende Abrechnung &amp; Payroll:</b>Unterstützung bei Lohn- und Gehalts­abrechnungen, einschließlich Pflege von Daten in PayDesk und Zeiterfassungssystemen.</p>
    <p><b>Personalbetreuung &amp; Verwaltung:</b>Umfassende Betreuung Ihrer Mitarbeiter und Sicherstellung reibungsloser Personal­prozesse.</p>
    <p><b>Betriebliches Eingliederungsmanage­ment (BEM):</b>Begleitung und Koordination von BEM-Pro­zessen zur erfolgreichen Wiedereingliede­rung nach längeren Krankheitsphasen.</p>
    <p><b>Zusammenarbeit mit Arbeitnehmerver­tretungen:</b>Unterstützung bei der Kommunikation und Verhandlungen mit Betriebsräten zu arbeitsrechtlichen Themen.</p>
    <p><b>Organisationsentwicklung &amp; Prozessver­besserung:</b>Analyse und Optimierung von Prozessen zur Steigerung der Effizienz und Flexibilität</p>
  </div>
  <div class="block" style="left:377px;top:492px;width:238px;height:42px;background:var(--dark)"></div>

  <div class="col services" style="left:622px;top:72px;width:92px">
    <p><b>Verfügbarkeit:</b>Ab sofort, Teilzeit / Vollzeit, flexibel nach Absprache</p>
    <p><b>Einsatzort:</b>Deutschlandweit remote, mit planbarer Reisetätig­keit. In Berlin/Branden­burg auch Hybrid möglich.</p>
  </div>
  <div class="photo" role="img" aria-label="Porträt der Freelancerin an einem Geländer am Flussufer mit Bürogebäuden" style="left:614px;top:189px;width:515px;height:345px;background:linear-gradient(100deg,#c9c3bc 0%,#8d7a6a 22%,#b8b2aa 45%,#9ea3a2 70%,#d2d0cc 100%)"></div>
  <div class="why-title" style="left:808px;top:236px">WARUM EIN HR-FREELANCER?</div>
  <div class="col services" style="left:833px;top:72px;width:130px">
    <p><b>Flexibilität</b>Freelancer können stundenweise oder projektbezogen engagiert wer­den – man bezahlt nur für tatsächlich benötigte Leistungen.</p>
    <p><b>Spezialisierte Expertise</b>Sie bringen Fachwissen aus ver­schiedenen Branchen mit und bieten sofortige Lösungen für spezifische HR-Aufgaben.</p>
    <p><b>Kosteneffizienz</b>Keine Fixkosten für Sozialleistungen, nur flexible Bezahlung nach Auf­wand.</p>
  </div>
  <div class="col services" style="left:970px;top:72px;width:128px">
    <p><b>Unabhängige Perspektive</b>Externe Freelancer bringen frische Ideen und können Prozesse objektiv bewerten und optimieren.</p>
    <p><b>Schnelle Verfügbarkeit</b>Freelancer sind sofort einsatzbereit und unterstützen kurzfristig bei Eng­pässen oder Projekten.</p>
    <p><b>Projektbezogene Unterstützung</b>Sie übernehmen zeitlich begrenzte Aufgaben und Projekte, von der Pla­nung bis zur Umsetzung.</p>
    <p><b>Netzwerk und Erfahrung</b>Durch Erfahrung in verschiedenen Unternehmen bieten sie wertvolle Kontakte und Best Practices.</p>
  </div>
  <div class="feature-box abs" style="left:832px;top:270px;width:265px;height:231px">
    <h3>Was mich auszeichnet</h3>
    <p class="k">Kommunikativ &amp; Organisiert:</p>
    <p class="v">Ich setze auf klare Kommunikation und strukturiertes Arbeiten.</p>
    <p class="k">Empathisch &amp; Diskret:</p>
    <p class="v">Der respektvolle Umgang mit Menschen ist mir wichtig.</p>
    <p class="k">Innovativ &amp; Teamfähig:</p>
    <p class="v">Immer offen für neue Ideen und eine starke Teamplayerin.</p>
  </div>
</section>

</body>
</html>
```